Tidewell Homes Website Redesign

We need a website redesign for an existing website www.tidewellhomes.com.au. A home page and a property page needs to be designed...have attached layout for property page which sits under House and Land.

Have also attached logo.

Site will be built on Pyx Frame Core 5x content management system so design needs to be PFC compatible and using system fonts as well eg Arial, Verdana or Tahoma.

Target Market(s)

Builders and owner builders

Industry/Entity Type

Construction

Number of Pages Required

2 pages

Requirements
Must have
• Site Map

• o Home
• o Inclusions
• o Designs
• o House and Land
• ? Gallery
• o Selection Centre
• o Redevelopment
• o Contact Us

• Design Brief

• o Likes www.ambrosecoastal.com.au as a corporate homepage layout...with buttons across the bottom etc
• o Likes http://www.valdrenhomes.com.au/
• o Likes http://www.corvask.com.au/, but this site is built entirely in flash so some functionality won’t be possible.
• • Logo and phone number across top 02 6378 9152
• • Rolling banner along bottom of page with gallery photos
• • Horizontal navigational bar
• • Content below the main menu
• • Large contact us button.
• - Need to ensure BTG and Guild Constructor logo is on every page (perhaps in footer???)
• - Need
• ACN 061 372 908 NSW License No. 483052K ACT License No. 3142
• also in footer of every page

• Colours are, maroon, gold and predominately white. I don"t have any problems with some elements of light grey.

```html
<!DOCTYPE html>
<html lang="en">
<head>
<meta charset="utf-8">
<title>Tidewell Homes – Home</title>
<link href="https://fonts.googleapis.com/css2?family=Yanone+Kaffeesatz:wght@400;500&family=PT+Sans:wght@400;700&display=swap" rel="stylesheet">
<style>
  :root{
    --maroon:#6b1640;
    --gold:#c9b45a;
    --gold-line:#d6c27a;
    --paper:#ece5d4;
    --panel:#ece2d6;
    --ink:#1e1a17;
    --dark:#2a211f;
    --tab:#1d1b1a;
    --side:#241c1a;
    --white:#ffffff;
    --grey-panel:#ebebeb;
  }
  *{box-sizing:border-box;margin:0;padding:0}
  html,body{width:986px;height:1200px;overflow:hidden}
  body{
    background:linear-gradient(90deg,#140f0e 0%,var(--side) 4%,#3a2d29 7%,var(--side) 7%) ;
    font-family:Tahoma,"PT Sans",Verdana,sans-serif;
    color:var(--ink);
    position:relative;
  }
  .display{font-family:"Yanone Kaffeesatz","Arial Narrow",sans-serif;font-weight:400}
  .page{
    position:absolute;left:69px;top:0;width:848px;height:1200px;
    background:radial-gradient(ellipse at 40% 30%,#f3eddf 0%,var(--paper) 55%,#e2d9c4 100%);
  }
  .call-now{position:absolute;right:26px;top:18px;font-size:27px;color:var(--maroon);letter-spacing:.3px}

  .brand{position:absolute;left:26px;top:126px;display:flex;align-items:center;gap:10px}
  .brand-mark{width:14px;height:14px;background:var(--maroon)}
  .brand-name{font-size:44px;color:var(--maroon);line-height:1}

  .banner{position:absolute;left:271px;top:66px;width:551px;height:241px;background:#cfc8b6;box-shadow:0 2px 5px rgba(0,0,0,.35)}
  .banner-photo{position:absolute;left:14px;top:13px;width:522px;height:167px;background:linear-gradient(90deg,#7a3a12 0%,#c98a4a 20%,#f1ede6 45%,#e9e3da 70%,#a5551f 100%)}
  .banner-caption{position:absolute;left:14px;top:180px;width:522px;height:48px;background:#0f0d0c;color:#ded29a;font-size:35px;text-align:center;line-height:48px}

  .nav{position:absolute;left:27px;top:323px;width:793px;height:29px;display:flex}
  .nav a{flex:auto;display:block;height:29px;line-height:30px;text-align:center;color:var(--white);font-size:12px;font-weight:bold;text-decoration:none;
    background:linear-gradient(#4a4746 0%,var(--tab) 45%,#0c0b0b 100%);border-right:1px solid #5d5a58;border-radius:5px 5px 0 0}
  .nav-rule{position:absolute;left:0;top:352px;width:848px;height:5px;background:var(--gold-line)}
  .nav-active{position:absolute;left:27px;top:352px;width:118px;height:7px;background:var(--maroon)}

  .welcome{position:absolute;left:27px;top:388px;width:562px}
  .welcome h1{font-size:27px;color:var(--ink);font-weight:400;padding-bottom:6px;border-bottom:2px dotted var(--gold)}
  .welcome h1 span{font-size:36px;color:var(--maroon)}
  .welcome .copy{padding-top:10px;height:307px;border-bottom:2px dotted var(--gold)}
  .welcome p{font-size:11.5px;line-height:16px;margin-bottom:16px}

  .card{position:absolute;background:var(--white);box-shadow:0 3px 5px rgba(0,0,0,.3);padding:6px}
  .card-inner{width:100%;height:100%;position:relative}
  .designs{left:603px;top:372px;width:230px;height:364px}
  .designs .card-inner{background:var(--panel)}
  .designs h2{position:absolute;left:8px;top:4px;font-size:24px;color:var(--maroon);font-weight:400}
  .design-list{position:absolute;left:6px;top:33px;width:206px;height:298px;background:var(--white);border-radius:8px;padding:4px 5px}
  .design-item{height:92px;margin-bottom:5px;border-radius:8px;box-shadow:0 0 3px rgba(0,0,0,.35);background:linear-gradient(#9cb3e6 0%,#e6eef8 50%,#8fb46a 85%)}
  .pager{position:absolute;right:6px;bottom:4px;font-size:13px;font-weight:bold;word-spacing:10px}

  .awards{left:14px;top:766px;width:565px;height:143px;padding:8px}
  .awards .card-inner{background:var(--grey-panel);text-align:center;padding-top:6px}
  .awards h3{font-size:18px;font-weight:400;color:var(--ink);margin-bottom:4px}
  .awards li{list-style:none;font-size:19px;color:var(--maroon);line-height:28px}

  .call-us{left:603px;top:766px;width:230px;height:143px}
  .call-us .card-inner{background:var(--panel);padding:14px 0 0 10px}
  .call-us .label{font-size:31px;color:var(--maroon);line-height:28px}
  .call-us .phone{font-size:24px;line-height:22px}
  .call-us .email-label{font-size:22px;color:var(--maroon);line-height:18px}
  .call-us .email{font-size:15px;line-height:16px}
  .call-us svg{position:absolute;right:6px;top:16px}

  .gallery{position:absolute;left:0;top:928px;width:848px;height:162px;background:linear-gradient(#1c1514,var(--dark) 60%,#3a302d)}
  .gallery h2{position:absolute;left:46px;top:8px;font-size:31px;color:var(--white);font-weight:400}
  .gallery .thumb{position:absolute;top:42px;width:189px;height:97px;background:var(--white);padding:6px}
  .gallery .thumb div{width:100%;height:100%}
  .gallery .arrow{position:absolute;top:95px}

  .footer{position:absolute;left:13px;top:1128px;width:520px}
  .footer .copyright{font-size:11px;font-weight:bold}
  .footer .licence{font-size:14px;margin-top:2px}
  .badge-a{position:absolute;left:628px;top:1103px;width:72px;height:84px;background:#0b6a4a;border-radius:14px 14px 30px 30px}
  .badge-b{position:absolute;left:735px;top:1106px;width:116px;height:80px;background:#23307a;border-radius:6px}
</style>
</head>
<body>
<div class="page">
  <div class="call-now display">CALL NOW : 02 6378 9152</div>

  <div class="brand">
    <span class="brand-mark"></span>
    <span class="brand-name display">Tidewell Homes</span>
  </div>

  <div class="banner">
    <div class="banner-photo" role="img" aria-label="Photo of a bright dining room with timber doors and a set table"></div>
    <div class="banner-caption display">we will build your home on budget and on time</div>
  </div>

  <nav class="nav">
    <a href="#">Home</a><a href="#">Inclusions</a><a href="#">Designs</a><a href="#">House &amp; Land</a><a href="#">Gallery</a><a href="#">Selection Centre</a><a href="#">Redevelopment</a><a href="#">Contact Us</a>
  </nav>
  <div class="nav-rule"></div>
  <div class="nav-active"></div>

  <section class="welcome">
    <h1 class="display">welcome to <span>Tidewell Homes Constructions</span></h1>
    <div class="copy">
      <p>Tidewell Homes Constructions was established in February 2001 by Owen Raskell and Lachlan Bretten. Between the two directors the company has over 40 years building experience in the ACT Region and both directors are individually licensed builders.</p>
      <p>We offer a range of flexible and varied home designs, these designs can be built on your land or ours. We will also quote individual designs should one of our plans be unsuitable to your needs or should you desire a more customized home.</p>
      <p>Tidewell Homes uses only quality suppliers and our team of contractors are reliable, qualified and assist us to achieve a quality finish.</p>
      <p>Both directors are hands on and personally oversee the construction process as well as being available to owners to attend to queries or concerns. Our aim is to build quality project homes whilst providing a boutique style service.</p>
      <p>Our efficient management of the construction process and our reliable team of contractors will ensure your new home is finished on time. This is why the Tidewell Homes guarantee is:</p>
    </div>
  </section>

  <aside class="card designs">
    <div class="card-inner">
      <h2 class="display">Designs</h2>
      <div class="design-list">
        <div class="design-item" role="img" aria-label="Illustration of a single-storey home design with garage"></div>
        <div class="design-item" role="img" aria-label="Illustration of a brick home design with trees"></div>
        <div class="design-item" role="img" aria-label="Illustration of a home design with flowering trees"></div>
      </div>
      <div class="pager">previous | next</div>
    </div>
  </aside>

  <section class="card awards">
    <div class="card-inner">
      <h3 class="display">Most Recently</h3>
      <ul class="display">
        <li>Winner BTG ‘ACT Energy Efficient Home of the Year’ 2005</li>
        <li>Finalist BTG ‘ACT Display Home of the Year’ 2005</li>
        <li>Finalist BTG ‘ACT House of the Year’ 2005</li>
      </ul>
    </div>
  </section>

  <aside class="card call-us">
    <div class="card-inner display">
      <div class="label">CALL US</div>
      <div class="phone">02 6378 9152</div>
      <div class="email-label">email:</div>
      <div class="email">support@tidewellhomes.com.au</div>
      <svg width="92" height="76" viewBox="0 0 92 76" aria-hidden="true">
        <path d="M6 22 Q46 -2 86 22 L80 34 L62 28 L60 18 Q46 12 32 18 L30 28 L12 34 Z" fill="#e8241c"/>
        <path d="M28 30 L64 30 L80 70 L12 70 Z" fill="#e8241c"/>
        <circle cx="46" cy="50" r="13" fill="#f3f0ea" stroke="#b81510" stroke-width="2"/>
        <circle cx="46" cy="50" r="4" fill="#b81510"/>
      </svg>
    </div>
  </aside>

  <section class="gallery">
    <h2 class="display">Photo Gallery</h2>
    <svg class="arrow" style="left:20px" width="15" height="15" viewBox="0 0 15 15" aria-hidden="true"><circle cx="7.5" cy="7.5" r="6.5" fill="none" stroke="#c8d84a" stroke-width="1.6"/><path d="M9.5 4 L5.5 7.5 L9.5 11" fill="none" stroke="#c8d84a" stroke-width="1.8"/></svg>
    <div class="thumb" style="left:45px"><div role="img" aria-label="Photo of a finished home facade with owners out front" style="background:linear-gradient(#bcc9d8 0%,#9b8770 40%,#6f5a48 100%)"></div></div>
    <div class="thumb" style="left:239px"><div role="img" aria-label="Photo of a bathroom with a corner spa" style="background:linear-gradient(#e7cf9a,#d8c3a0)"></div></div>
    <div class="thumb" style="left:433px"><div role="img" aria-label="Photo of a dining area looking onto a lawn" style="background:linear-gradient(90deg,#3d3530,#9aa48a 50%,#6c8a4a)"></div></div>
    <div class="thumb" style="left:627px"><div role="img" aria-label="Photo of a home with a timber deck" style="background:linear-gradient(#d7d2c8,#a0603a 60%,#5b4632)"></div></div>
    <svg class="arrow" style="left:830px" width="15" height="15" viewBox="0 0 15 15" aria-hidden="true"><circle cx="7.5" cy="7.5" r="6.5" fill="none" stroke="#c8d84a" stroke-width="1.6"/><path d="M5.5 4 L9.5 7.5 L5.5 11" fill="none" stroke="#c8d84a" stroke-width="1.8"/></svg>
  </section>

  <footer class="footer">
    <div class="copyright">Copyright 2010, tidewellhomes.com.au</div>
    <div class="licence">ACN 061 372 908 NSW License No. 483052K ACT License No. 3142</div>
  </footer>
  <div class="badge-a" role="img" aria-label="BTG membership badge"></div>
  <div class="badge-b" role="img" aria-label="Guild Constructor membership badge"></div>
</div>
</body>
</html>
```